KFR T Coaching Website

We need a website to post videos, blogs and other information or links.
We teach Jujitsu , combatives, Metaphysical Coaching. I want to tach online and in person. Silver Harbor Institute Deals in several areas of Personal Protection and Coaching.
Training (Martial Arts / combative)
Emotional Intelligence
Leadership Development
Motivation
Our Log is attached.
Similar Websites to what we do ( we want to stand out better).
https://renwoskel.com/
https://bavomure.com/
https://crestlinevigorcoaching.com/
Training , Martial Arts, coaching
2 page

```html
<!DOCTYPE html>
<html lang="en">
<head>
<meta charset="utf-8">
<title>KFR T Coaching — Website</title>
<link href="https://fonts.googleapis.com/css2?family=Montserrat:wght@400;500;600&display=swap" rel="stylesheet">
<style>
:root{
  --stage:#a9a5a4;
  --header:#1b1d22;
  --header-glow:#3a1016;
  --hero-dark:#060203;
  --hero-red:#5a0d13;
  --footer:#1d1d1f;
  --red:#e23a3f;
  --white:#f4f4f4;
  --muted:#5b5b5e;
  --rule:#3a3b40;
}
*{margin:0;padding:0;box-sizing:border-box}
html,body{width:1200px;height:1148px;overflow:hidden}
body{background:var(--stage);font-family:"Montserrat",sans-serif;color:var(--white);position:relative;text-transform:uppercase}
.red{color:var(--red)}

/* ---------- desktop page ---------- */
.desktop{position:absolute;left:410px;top:140px;width:722px;height:868px;overflow:hidden;background:var(--hero-dark);box-shadow:0 10px 30px rgba(0,0,0,.35)}
.desktop .site-header{position:absolute;left:0;top:0;width:100%;height:79px;background:radial-gradient(ellipse 45% 120% at 62% 0%,var(--header-glow),var(--header) 70%)}
.brand{position:absolute;display:flex;align-items:center;gap:8px}
.brand-mark{background:var(--white);flex:none}
.brand-name{color:var(--white);font-weight:500;letter-spacing:.14em;line-height:1.15}
.desktop .brand{left:109px;top:13px}
.desktop .brand-mark{width:26px;height:26px}
.desktop .brand-name{font-size:11px}
.main-nav{position:absolute;left:109px;top:55px;width:503px;border-top:1px solid var(--rule);height:24px;display:flex;align-items:center;gap:0}
.main-nav a{font-size:6.6px;letter-spacing:.09em;color:var(--white);text-decoration:none;font-weight:500;margin-right:16px;position:relative}
.main-nav a.active{color:var(--red)}
.main-nav a.active::before{content:"";position:absolute;left:0;top:-9px;width:34px;height:1px;background:var(--red)}
.main-nav .search{position:absolute;right:2px;top:9px}

.hero-photo{position:absolute;background:
  radial-gradient(ellipse 40% 45% at 72% 40%,#6b1a1c 0%,rgba(90,13,19,.6) 45%,transparent 75%),
  linear-gradient(100deg,var(--hero-dark) 25%,#2a0507 55%,var(--hero-red) 75%,#1a0304 100%)}
.desktop .hero{position:absolute;left:0;top:79px;width:722px;height:592px}
.desktop .hero-photo{inset:0}
.pillars{position:absolute;font-weight:500}
.pillars li{list-style:none;letter-spacing:.12em;white-space:nowrap}
.desktop .pillars{left:106px;top:174px}
.desktop .pillars li{font-size:17px;margin-bottom:24px}
.desktop .pillars li.first{margin-bottom:18px;line-height:1}
.pillars .sub{display:block;color:var(--white);letter-spacing:.1em}
.desktop .pillars .sub{font-size:9.5px;margin-top:6px;margin-left:2px}

.partner-mark{position:absolute;display:flex;flex-direction:column;align-items:center;color:var(--muted);font-weight:600;letter-spacing:.02em;text-align:center;line-height:1.1}
.partner-mark .square{background:var(--muted)}
.desktop .partner-mark{left:88px;top:400px;width:200px;font-size:18px}
.desktop .partner-mark .square{width:70px;height:70px;margin-bottom:16px}

.slide-arrow{position:absolute}
.desktop .arrow-next{left:670px;top:279px}
.desktop .arrow-prev{left:-16px;top:279px}

.site-footer{position:absolute;left:0;width:100%;background:var(--footer)}
.desktop .site-footer{top:671px;height:197px}
.footer-badge{position:absolute;background:#fff;display:flex;align-items:center;justify-content:center;color:#111;font-weight:600;text-align:center;letter-spacing:.02em}
.desktop .footer-badge{left:117px;top:25px;width:173px;height:109px;font-size:10px}
.about{position:absolute}
.about h2{font-weight:500;letter-spacing:.12em}
.about p{letter-spacing:.06em;line-height:1.55}
.desktop .about{left:302px;top:30px;width:290px}
.desktop .about h2{font-size:11.5px;margin-bottom:12px}
.desktop .about p{font-size:5.6px;margin-bottom:8px}
.desktop .footer-rule{position:absolute;left:109px;top:152px;width:503px;border-top:1px solid var(--rule)}
.desktop .copyright{position:absolute;left:0;top:168px;width:100%;text-align:center;font-size:7.2px;letter-spacing:.1em}

/* ---------- mobile page ---------- */
.mobile{position:absolute;left:60px;top:300px;width:293px;height:663px;overflow:hidden;background:var(--hero-dark);box-shadow:0 10px 30px rgba(0,0,0,.35)}
.mobile .site-header{position:absolute;left:0;top:0;width:100%;height:143px;background:radial-gradient(ellipse 80% 90% at 70% 10%,var(--header-glow),var(--header) 75%);border-bottom:1px solid var(--rule)}
.mobile .brand{left:0;top:20px;width:100%;flex-direction:column;gap:12px;text-align:center}
.mobile .brand-mark{width:50px;height:50px}
.mobile .brand-name{font-size:19px}
.mobile-bar{position:absolute;left:0;top:143px;width:100%;height:40px;background:var(--header);border-bottom:2px solid #2a2b30}
.mobile-bar .menu{position:absolute;left:7px;top:13px}
.mobile-bar .search{position:absolute;right:10px;top:13px}
.mobile .hero{position:absolute;left:0;top:185px;width:293px;height:360px}
.mobile .hero-photo{inset:0}
.mobile .pillars{left:23px;top:116px}
.mobile .pillars li{font-size:9.5px;margin-bottom:17px}
.mobile .pillars li.first{margin-bottom:9px;line-height:1}
.mobile .pillars .sub{font-size:6.3px;margin-top:3px}
.mobile .partner-mark{left:14px;top:232px;width:140px;font-size:11px}
.mobile .partner-mark .square{width:44px;height:44px;margin-bottom:10px}
.mobile .site-footer{top:545px;height:118px}
.mobile .footer-badge{left:13px;top:22px;width:117px;height:74px;font-size:7px}
.mobile .about{left:140px;top:22px;width:142px}
.mobile .about h2{font-size:10.5px;margin-bottom:9px}
.mobile .about p{font-size:5.5px}
.to-top{position:absolute;left:255px;top:633px;width:28px;height:29px;background:var(--red);border-radius:3px;display:flex;align-items:center;justify-content:center}
</style>
</head>
<body>

<section class="mobile" aria-label="KFR T Coaching mobile home page">
  <header class="site-header">
    <div class="brand"><span class="brand-mark"></span><span class="brand-name">KFR T<br>Coaching</span></div>
  </header>
  <div class="mobile-bar">
    <svg class="menu" width="15" height="13" viewBox="0 0 15 13"><rect y="0" width="15" height="2.6" fill="#fff"/><rect y="5.2" width="15" height="2.6" fill="#fff"/><rect y="10.4" width="15" height="2.6" fill="#fff"/></svg>
    <svg class="search" width="10" height="10" viewBox="0 0 10 10"><circle cx="4" cy="4" r="3" fill="none" stroke="#fff" stroke-width="1.6"/><line x1="6.2" y1="6.2" x2="9.3" y2="9.3" stroke="#fff" stroke-width="1.8"/></svg>
  </div>
  <div class="hero">
    <div class="hero-photo" role="img" aria-label="Photo of a woman in red boxing gloves throwing a punch against a dark red backdrop"></div>
    <ul class="pillars">
      <li class="first red">Training<span class="sub">(Martial Arts / Combative)</span></li>
      <li><span class="red">Emotional</span> Intelligence</li>
      <li><span class="red">Leadership</span> Development</li>
      <li class="red">Motivation</li>
    </ul>
    <div class="partner-mark"><span class="square"></span>Silver Harbor Institute</div>
  </div>
  <footer class="site-footer">
    <div class="footer-badge">Silver Harbor<br>Institute</div>
    <div class="about">
      <h2><span class="red">KFR T</span> Coaching</h2>
      <p>Lorem ipsum dolor sit amet, consectetur adipiscing elit. Mauris rhoncus, mi id bibendum malesuada, velit tellus tempus nunc, ut commodo leo lacus commodo odio. Nulla facilisi. Integer id nibh magna. Nam sed efficitur nulla.</p>
    </div>
  </footer>
  <a class="to-top" aria-label="Back to top"><svg width="10" height="6" viewBox="0 0 10 6"><polyline points="1,5 5,1 9,5" fill="none" stroke="#fff" stroke-width="1.3"/></svg></a>
</section>

<section class="desktop" aria-label="KFR T Coaching desktop home page">
  <div class="hero">
    <div class="hero-photo" role="img" aria-label="Photo of a woman in red boxing gloves throwing a punch against a dark red backdrop"></div>
    <svg class="slide-arrow arrow-prev" width="34" height="34" viewBox="0 0 34 34"><circle cx="17" cy="17" r="15.5" fill="none" stroke="#3a2a2c" stroke-width="2"/><polyline points="19,10 12,17 19,24" fill="none" stroke="#3a2a2c" stroke-width="2"/><line x1="12" y1="17" x2="25" y2="17" stroke="#3a2a2c" stroke-width="2"/></svg>
    <svg class="slide-arrow arrow-next" width="34" height="34" viewBox="0 0 34 34"><circle cx="17" cy="17" r="15.5" fill="none" stroke="#3a2a2c" stroke-width="2"/><polyline points="15,10 22,17 15,24" fill="none" stroke="#3a2a2c" stroke-width="2"/><line x1="9" y1="17" x2="22" y2="17" stroke="#3a2a2c" stroke-width="2"/></svg>
    <ul class="pillars">
      <li class="first red">Training<span class="sub">(Martial Arts / Combative)</span></li>
      <li><span class="red">Emotional</span> Intelligence</li>
      <li><span class="red">Leadership</span> Development</li>
      <li class="red">Motivation</li>
    </ul>
    <div class="partner-mark"><span class="square"></span>Silver Harbor Institute</div>
  </div>
  <header class="site-header">
    <div class="brand"><span class="brand-mark"></span><span class="brand-name">KFR T<br>Coaching</span></div>
    <nav class="main-nav">
      <a class="active">KFR T</a><a>Products</a><a>Services</a><a>Schedule</a><a>Contact Us</a>
      <svg class="search" width="6" height="6" viewBox="0 0 10 10"><circle cx="4" cy="4" r="3" fill="none" stroke="#fff" stroke-width="1.8"/><line x1="6.2" y1="6.2" x2="9.3" y2="9.3" stroke="#fff" stroke-width="2"/></svg>
    </nav>
  </header>
  <footer class="site-footer">
    <div class="footer-badge">Silver Harbor<br>Institute</div>
    <div class="about">
      <h2><span class="red">KFR T</span> Coaching</h2>
      <p>Lorem ipsum dolor sit amet, consectetur adipiscing elit. Mauris rhoncus, mi id bibendum malesuada, velit tellus tempus nunc, ut commodo leo lacus commodo odio. Nulla facilisi. Integer id nibh magna. Nam sed efficitur nulla.</p>
      <p>Aliquam ac neque at sem sodales eleifend rutrum a neque. Ut volutpat nisi non venenatis molestie. Vestibulum ultricies, ipsum ac pulvinar venenatis, risus est lobortis magna, nec cursus diam felis vitae sem. Etiam eu mollis ex. Nullam nec nisi urna. Faucibus risus sit amet diam molestie luctus.</p>
    </div>
    <div class="footer-rule"></div>
    <p class="copyright">Copyright © 2022 <span class="red">KFR T</span> Coaching. All rights reserved.</p>
  </footer>
</section>

</body>
</html>
```